Consulting company needs Business Cards - rough concept provided

I'm looking for someone to take our business card idea and make is slick and polished - to communicate our high-end, sophisticated, serious consulting business. We have a rough layout we did in-house. We are open to ideas on repo-ing elements, adjusting sizes, typefaces etc... within the general concept we've already come up with. We want it to be super-clean and sophisticated. We want to keep the white backgrounds, and blue brand colors. Our goal is to print with painted blue edges on thick cardstock. Thank you!!

```html
<!DOCTYPE html>
<html lang="en">
<head>
<meta charset="utf-8">
<title>Nordvale Consulting — Stationery</title>
<link rel="stylesheet" href="https://fonts.googleapis.com/css2?family=Open+Sans:wght@700&family=EB+Garamond:ital,wght@0,400;0,600;1,400&display=swap">
<style>
  :root {
    --bg: #ecebe8;
    --paper: #f8f8f6;
    --blue: #1477d2;
    --blue-soft: #d3e5f6;
    --ink: #2b2b2b;
    --motif: #f0f0ed;
    --sans: "Open Sans", Arial, sans-serif;
    --serif: "EB Garamond", Georgia, serif;
  }
  * { margin: 0; padding: 0; box-sizing: border-box; }
  html, body { width: 1200px; height: 801px; overflow: hidden; background: var(--bg); }
  .canvas { position: relative; width: 1200px; height: 801px; }
  .piece { position: absolute; background: var(--paper); overflow: hidden; }
  .piece svg.art { position: absolute; inset: 0; }
  .wordmark { position: absolute; font-family: var(--sans); font-weight: 700; color: var(--blue); letter-spacing: -0.5px; white-space: nowrap; }
  .serif-block { position: absolute; font-family: var(--serif); color: var(--ink); font-size: 8px; line-height: 1.5; letter-spacing: 0.15px; white-space: nowrap; }
  .serif-block .caps { text-transform: uppercase; letter-spacing: 0.3px; }
  .url { font-family: var(--sans); font-weight: 700; color: var(--blue); font-size: 7px; letter-spacing: 0; }

  /* Letterhead */
  .letterhead { left: 48px; top: 39px; width: 515px; height: 718px; }
  .letterhead .wordmark { left: 33px; top: 28px; font-size: 24px; }
  .letterhead .accent-rule { position: absolute; left: 33px; top: 143px; width: 31px; height: 1.5px; background: var(--blue); }
  .letterhead .tagline { left: 33px; top: 158px; font-style: italic; font-size: 9px; line-height: 1.55; }
  .letterhead .address { left: 368px; top: 158px; }
  .letterhead .address p + p { margin-top: 6px; }

  /* Envelope front */
  .envelope-front { left: 607px; top: 44px; width: 549px; height: 247px; }
  .envelope-front .wordmark { left: 30px; top: 29px; font-size: 24px; }
  .envelope-front .address { left: 32px; top: 86px; }

  /* Envelope back */
  .envelope-back { left: 608px; top: 317px; width: 549px; height: 238px; }
  .envelope-back .flap-name { position: absolute; left: 0; right: 0; top: 28px; text-align: center; font-family: var(--sans); font-weight: 700; font-size: 24px; color: var(--blue-soft); letter-spacing: -0.5px; }
  .envelope-back .url { position: absolute; left: 0; width: 530px; text-align: center; top: 211px; }

  /* Business cards */
  .card { border: 3px solid var(--blue); }
  .card-front { left: 614px; top: 588px; width: 226px; height: 143px; }
  .card-front .wordmark { left: 0; right: 0; top: 53px; text-align: center; font-size: 22px; }
  .card-back { left: 884px; top: 588px; width: 253px; height: 145px; border-width: 2px; }
  .card-back .contact { left: 19px; top: 63px; font-size: 7.5px; }
  .card-back .contact .name { font-weight: 600; text-transform: uppercase; letter-spacing: 0.4px; }
  .card-back .contact .gap { margin-top: 8px; }
</style>
</head>
<body>
<main class="canvas">

  <!-- Letterhead -->
  <section class="piece letterhead" aria-label="Letterhead">
    <svg class="art" width="515" height="718" viewBox="0 0 515 718">
      <text x="270" y="127" font-family="Open Sans, sans-serif" font-weight="700" font-size="170" fill="#efefec">NO</text>
      <rect x="395" y="276" width="120" height="342" fill="var(--motif)" role="img" aria-label="Faint architectural line drawing"/>
      <text x="-22" y="770" font-family="Open Sans, sans-serif" font-weight="700" font-size="380" fill="var(--blue)" letter-spacing="-10">NO</text>
    </svg>
    <div class="wordmark">NORDVALE</div>
    <div class="accent-rule"></div>
    <div class="serif-block tagline">Strategy.<br>Transformation.<br>Impact.</div>
    <div class="serif-block address">
      <p><span class="caps">Nordvale Consulting</span></p>
      <p>40 Meridian Street<br>New York, NY 10016<br>United States</p>
      <p>info@nordvale.com<br>+1 212 555 0147</p>
      <p class="url">nordvale.com</p>
    </div>
  </section>

  <!-- Envelope front -->
  <section class="piece envelope-front" aria-label="Envelope front">
    <svg class="art" width="549" height="247" viewBox="0 0 549 247">
      <rect x="270" y="78" width="100" height="169" fill="var(--motif)" role="img" aria-label="Faint architectural line drawing"/>
      <text x="352" y="220" font-family="Open Sans, sans-serif" font-weight="700" font-size="212" fill="var(--blue)" letter-spacing="-6">NO</text>
    </svg>
    <div class="wordmark">NORDVALE</div>
    <div class="serif-block address">
      <span class="caps">Nordvale Consulting</span><br>40 Meridian Street<br>New York, NY 10016<br>United States
    </div>
  </section>

  <!-- Envelope back -->
  <section class="piece envelope-back" aria-label="Envelope back">
    <svg class="art" width="549" height="238" viewBox="0 0 549 238">
      <line x1="0" y1="238" x2="50" y2="86" stroke="#d6d6d3" stroke-width="0.7"/>
      <line x1="549" y1="238" x2="500" y2="86" stroke="#d6d6d3" stroke-width="0.7"/>
      <rect x="389" y="96" width="110" height="142" fill="var(--motif)" role="img" aria-label="Faint architectural line drawing"/>
      <path d="M0 0 H549 L510 78 Q506 86 496 86 H52 Q42 86 38 78 Z" fill="var(--blue)"/>
    </svg>
    <div class="flap-name">NORDVALE</div>
    <div class="url">nordvale.com</div>
  </section>

  <!-- Business card front -->
  <section class="piece card card-front" aria-label="Business card front">
    <div class="wordmark">NORDVALE</div>
  </section>

  <!-- Business card back -->
  <section class="piece card card-back" aria-label="Business card back">
    <svg class="art" width="249" height="141" viewBox="0 0 249 141">
      <text x="104" y="132" font-family="Open Sans, sans-serif" font-weight="700" font-size="175" fill="var(--blue)" letter-spacing="-8">NO</text>
    </svg>
    <div class="serif-block contact">
      <div class="name">Daniel Reyes</div>
      <div>Managing Partner</div>
      <div class="gap">daniel@nordvale.com<br>+1 212 555 0147</div>
      <div class="gap url">nordvale.com</div>
    </div>
  </section>

</main>
</body>
</html>
```